Brantley Studios photography and video creator

I need a business card for my production company. I shoot photography and videography for real estate, adventure sports and businesses

Contact Information for Business Card

simple not to busy

Colors

Designer to choose colors to be used in the design.

Requirements
Must have
• derek@brantleystudios.ca
• phone -5873304127
• instagram derek_brantley

```html
<!DOCTYPE html>
<html lang="en">
<head>
<meta charset="utf-8">
<title>Brantley Studios — Business Card</title>
<link rel="stylesheet" href="https://fonts.googleapis.com/css2?family=Montserrat:wght@400;500;700;800&display=swap">
<style>
  :root {
    --page: #d9d9d9;
    --card: #f4f4f4;
    --ink: #1b1b1b;
    --ink-soft: #3a3a3a;
    --paper-white: #ffffff;
    --sky: #f1f1f1;
    --ridge-light: #cfcfcf;
    --ridge-mid: #8a8a8a;
    --ridge-dark: #1c1c1c;
  }
  * { margin: 0; padding: 0; box-sizing: border-box; }
  html, body {
    width: 1200px;
    height: 1021px;
    overflow: hidden;
    background: var(--page);
    font-family: "Montserrat", sans-serif;
  }
  .card {
    position: absolute;
    width: 700px;
    height: 400px;
    border-radius: 4px;
    overflow: hidden;
    box-shadow: 0 10px 30px rgba(0,0,0,0.25);
  }
  .card--front {
    left: 420px;
    top: 70px;
    background: var(--card);
    display: flex;
    align-items: center;
    justify-content: center;
  }
  .brand {
    display: flex;
    align-items: center;
    gap: 16px;
  }
  .brand__dot {
    width: 40px;
    height: 40px;
    border-radius: 50%;
    background: var(--ink);
  }
  .brand__name {
    font-weight: 800;
    font-size: 40px;
    letter-spacing: 1px;
    text-transform: uppercase;
    color: var(--ink);
  }
  .card--back {
    left: 80px;
    top: 540px;
  }
  .card__scene {
    position: absolute;
    inset: 0;
    background: linear-gradient(180deg,
      var(--sky) 0%,
      var(--sky) 30%,
      var(--ridge-light) 42%,
      var(--ridge-mid) 52%,
      var(--ridge-dark) 64%,
      var(--ridge-dark) 100%);
  }
  .person {
    position: absolute;
    right: 70px;
    top: 112px;
    text-align: right;
  }
  .person__name {
    font-weight: 700;
    font-size: 22px;
    letter-spacing: 0.5px;
    color: var(--ink);
    text-transform: uppercase;
  }
  .person__role {
    font-weight: 500;
    font-size: 17px;
    color: var(--ink-soft);
    margin-top: 2px;
  }
  .contact {
    position: absolute;
    right: 70px;
    bottom: 50px;
    list-style: none;
    text-align: right;
    color: var(--paper-white);
    font-size: 18px;
    font-weight: 400;
    line-height: 30px;
  }
  .contact__item {
    display: flex;
    align-items: center;
    justify-content: flex-end;
    gap: 10px;
  }
  .contact__icon {
    width: 16px;
    height: 16px;
    flex: none;
  }
</style>
</head>
<body>
  <section class="card card--front">
    <div class="brand">
      <span class="brand__dot"></span>
      <span class="brand__name">Brantley Studios</span>
    </div>
  </section>

  <section class="card card--back">
    <div class="card__scene" role="img" aria-label="Layered grey mountain ridges with a tall pine tree silhouette"></div>
    <div class="person">
      <div class="person__name">Derek Brantley</div>
      <div class="person__role">Photographer</div>
    </div>
    <ul class="contact">
      <li class="contact__item">
        <span>587-330-4127</span>
        <svg class="contact__icon" viewBox="0 0 24 24" aria-hidden="true">
          <path fill="currentColor" d="M6.6 10.8a15.2 15.2 0 0 0 6.6 6.6l2.2-2.2a1 1 0 0 1 1-.25 11.4 11.4 0 0 0 3.6.6 1 1 0 0 1 1 1V20a1 1 0 0 1-1 1A17 17 0 0 1 3 4a1 1 0 0 1 1-1h3.5a1 1 0 0 1 1 1c0 1.25.2 2.45.6 3.6a1 1 0 0 1-.25 1z"/>
        </svg>
      </li>
      <li class="contact__item">
        <span>derek@brantleystudios.ca</span>
        <svg class="contact__icon" viewBox="0 0 24 24" aria-hidden="true">
          <rect x="2.5" y="5" width="19" height="14" fill="none" stroke="currentColor" stroke-width="2"/>
          <path d="M2.5 5l9.5 8 9.5-8" fill="none" stroke="currentColor" stroke-width="2"/>
        </svg>
      </li>
      <li class="contact__item">
        <span>derek_brantley</span>
        <svg class="contact__icon" viewBox="0 0 24 24" aria-hidden="true">
          <circle cx="12" cy="12" r="9" fill="none" stroke="currentColor" stroke-width="2"/>
        </svg>
      </li>
    </ul>
  </section>
</body>
</html>
```